Business Card Design Project

I need a business card design for an Organic drive thru coffee kiosk. We will serve organic coffee, teas & smoothies and will serve healthy breakfast food/snacks for people on the go.
I want the card to have 2-3 colors max (earthy colors like browns, greens and so on).
I have attached the logo I want used and would love to play off the theme of "balance."
Include:
Sun-Grove Coffee
address: 4170 Pelham Ct. Raleigh, NC 27593
phone: 919-307-4462
website: www.sun-grove-example.com (website is not up yet but still include it on card)
email: Dorothy@sun-grove-example.com
I want one of the following sayings somewhere on the card (the front or back is fine):
"Eat & Drink Well, on the run!"
"Break the fast with Sun-Grove"
Maybe on the back list what we offer:
-Organic coffee, espresso & tea
-Blendora smoothies & protein shakes
-Zesty Tonic (100% fresh local fruit and veggies)
-Healthy Bites

```html
<!DOCTYPE html>
<html lang="en">
<head>
<meta charset="utf-8">
<title>Sun-Grove Coffee – Business Card</title>
<link rel="stylesheet" href="https://fonts.googleapis.com/css2?family=Asap+Condensed:wght@400;500;600&display=swap">
<style>
  :root {
    --backdrop: #3d2b22;
    --roast-brown: #7b3b27;
    --roast-brown-dark: #5f2c1d;
    --honey: #e9a94a;
    --honey-light: #f3cf8f;
    --cream: #fbf3ea;
    --muted-rose: #c9a49a;
    --bean-grey: #8a7f86;
    --espresso-ink: #5b3420;
  }
  * { box-sizing: border-box; margin: 0; padding: 0; }
  html, body {
    width: 1200px;
    height: 871px;
    overflow: hidden;
    background: var(--backdrop);
  }
  .canvas {
    width: 1200px;
    height: 871px;
    display: flex;
    align-items: center;
    justify-content: center;
    gap: 50px;
    font-family: "Asap Condensed", "Arial Narrow", sans-serif;
  }
  .card {
    position: relative;
    width: 540px;
    height: 310px;
    border-radius: 0 150px 0 150px;
    overflow: hidden;
  }
  /* Front */
  .card--front {
    background: linear-gradient(160deg, var(--roast-brown) 0%, var(--roast-brown-dark) 100%);
    color: var(--cream);
  }
  .brand {
    position: absolute;
    left: 48px;
    top: 60px;
  }
  .brand__name {
    display: flex;
    align-items: center;
    gap: 14px;
    font-size: 62px;
    font-weight: 500;
    line-height: 1;
    letter-spacing: 0.5px;
  }
  .brand__dot {
    width: 46px;
    height: 46px;
    border: 3px solid currentColor;
    border-radius: 50%;
    flex: none;
  }
  .brand__tagline {
    margin-top: 8px;
    margin-left: 60px;
    font-size: 17px;
    letter-spacing: 3.2px;
    font-weight: 500;
  }
  .contact {
    position: absolute;
    right: 46px;
    bottom: 40px;
    list-style: none;
    color: var(--muted-rose);
    font-size: 16px;
    line-height: 1.4;
  }
  /* Back */
  .card--back {
    background: linear-gradient(200deg, var(--honey-light) 0%, var(--honey) 55%, #d68d2c 100%);
    color: var(--espresso-ink);
  }
  .back-brand {
    position: absolute;
    left: 44px;
    top: 50px;
    display: flex;
    align-items: center;
    gap: 14px;
    color: var(--bean-grey);
    font-size: 58px;
    font-weight: 500;
    line-height: 1;
  }
  .back-brand .brand__dot { width: 44px; height: 44px; }
  .saying {
    position: absolute;
    left: 46px;
    top: 140px;
    font-size: 24px;
    font-weight: 600;
  }
  .offerings {
    position: absolute;
    left: 48px;
    top: 182px;
    list-style: none;
    font-size: 15px;
    line-height: 1.45;
  }
  .offerings li::before { content: "– "; }
</style>
</head>
<body>
<main class="canvas">
  <section class="card card--front" aria-label="Card front">
    <div class="brand">
      <div class="brand__name"><span class="brand__dot"></span>Sun-Grove</div>
      <div class="brand__tagline">ORGANIC COFFEE + CAFE</div>
    </div>
    <ul class="contact">
      <li>Sun-Grove Coffee</li>
      <li>4170 Pelham Ct. Raleigh, NC 27593</li>
      <li>919-307-4462</li>
      <li>www.sun-grove-example.com</li>
      <li>Dorothy@sun-grove-example.com</li>
    </ul>
  </section>

  <section class="card card--back" aria-label="Card back">
    <div class="back-brand"><span class="brand__dot"></span>Sun-Grove</div>
    <p class="saying">Eat &amp; Drink Well, on the run!</p>
    <ul class="offerings">
      <li>Organic coffee, espresso &amp; tea</li>
      <li>Blendora smoothies &amp; protein shakes</li>
      <li>Zesty Tonic (100% fresh local fruit and veggies)</li>
      <li>Healthy Bites</li>
    </ul>
  </section>
</main>
</body>
</html>
```